Flyer-Design für Hundephysiopraxis
Zielgruppe
Ich bin selbstständige Hundephysiotherapeutin / Hundeosteopathin /Hundefitnesstrainerin. Meine Zielgruppe sind Hundehalter bzw. allgemein Tierhalter (biete noch weitere Dinge für Hunde/Tiere an) aber auch Tierärzte.
Aufgabenstellung
Es wäre schön, wenn Sie die Texte ähnlich wie auf meiner Homepage gestalten (z.B. Infos aus der Startseite oder Therapieformen).
Prinzipiell sollte es eher natürlich, freundlich und nett gestaltet sein. Schlichtere Farben passend zum Logo.
Homepage: www.pfotenruhe-mitte.de
Bei den Maßen bin ich offen, hatte aber eher an diesen 'typischen Flyer' gedacht (3 seitiger Flyer mit Vorder und Rückseite) bin aber prinzipiell offen :)
Einen Beispiel Flyer habe ich drangehängt sowie z.B. schon ein paar Fotos die man ggf nutzen kann. Weitere Behandlunsfotos kann ich gerne nachreichen.
Die Flyer sollen hauptsächlich bei z.B. Tierärzten / Tierklinik / Tiernahrungsmärkte wie Napfkorb ausgelegt werden damit Menschen die mich noch nicht kennen auf meine Arbeit aufmerksam werden.

```html
<!DOCTYPE html>
<html lang="de">
<head>
<meta charset="utf-8">
<title>Pfotenruhe Mitte – Flyer</title>
<link href="https://fonts.googleapis.com/css2?family=Dancing+Script:wght@500;600&family=Roboto:wght@400;500;700&display=swap" rel="stylesheet">
<style>
:root{
  --bg:#ebdfd7;
  --paper:#ffffff;
  --peach:#f4aa7a;
  --peach-light:#fce7dc;
  --accent:#e0622a;
  --heading:#b5452a;
  --text:#2f2f2f;
  --photo-green:#6f9a3c;
  --photo-dark:#3a3a3a;
}
*{box-sizing:border-box;margin:0;padding:0}
html,body{width:853px;height:1200px;overflow:hidden;background:var(--bg)}
body{position:relative;font-family:'Roboto',sans-serif;color:var(--text)}
.sheet{position:absolute;left:83px;width:687px;height:490px;background:var(--paper);box-shadow:8px 10px 10px rgba(0,0,0,.18);overflow:hidden}
.sheet--outside{top:88px}
.sheet--inside{top:626px}
.abs{position:absolute}
.script{font-family:'Dancing Script',cursive;color:var(--heading);font-weight:600}
.h-service{font-size:14.5px;text-align:center;width:200px}
.body{font-size:7px;line-height:9.5px}
.center{text-align:center}
.badge{position:absolute;border-radius:50%;background:var(--accent);display:flex;align-items:center;justify-content:center}
.dot{position:absolute;border-radius:50%;background:var(--accent)}
.photo-circle{border-radius:50%;border:1.3px solid var(--accent);padding:3px;background:#fff}
.photo-circle .fill{width:100%;height:100%;border-radius:50%}
.photo-frame{position:absolute;border:1.3px solid var(--accent);border-radius:11px;padding:4px;background:#fff}
.photo-frame .fill{width:100%;height:100%;border-radius:8px}
.float-circle{float:right;width:70px;height:70px;shape-outside:circle(50%);margin-left:4px}
.float-circle-left{float:left;width:70px;height:70px;shape-outside:circle(50%);margin-right:6px}
.fill--dog{background:linear-gradient(160deg,#5a5a5a,#1f1f1f 60%,#4a4a4a)}
.fill--garden{background:linear-gradient(180deg,#8a8f86 0%,#b8a9a0 40%,var(--photo-green) 75%,#4f7a2a 100%)}
.fill--spaniel{background:linear-gradient(180deg,#6c7e3f 0%,#85a64a 30%,#2b2b2b 55%,#9a9a9a 80%,#7fa446 100%)}
.fill--puppy{background:linear-gradient(160deg,#efe1cf,#d9b98e)}
.fill--lawn{background:linear-gradient(180deg,#7c9d48,#5f8a30)}
.fill--stone{background:linear-gradient(150deg,#505050,#2a2a2a 50%,#6aa59a 70%,#333)}
.services{font-size:5px;font-weight:700;color:#fff;line-height:7.4px;text-align:center;width:220px}
.speech{position:absolute;left:18px;width:204px;border:1.3px solid var(--accent);border-radius:6px;padding:4px 6px;font-size:7px;line-height:9.5px;background:#fff}
.speech::after{content:"";position:absolute;right:14px;bottom:-6px;width:10px;height:10px;background:#fff;border-right:1.3px solid var(--accent);border-bottom:1.3px solid var(--accent);transform:rotate(45deg)}
.list{font-size:7px;line-height:9.5px;list-style:none}
.brand-name{font-family:'Roboto',sans-serif;font-weight:500;color:var(--accent);font-size:13px}
.brand-tag{font-size:5.5px;letter-spacing:1px;color:var(--accent)}
</style>
</head>
<body>

<!-- Outside -->
<section class="sheet sheet--outside">
  <svg class="abs" style="left:0;top:0" width="687" height="490" viewBox="0 0 687 490" aria-hidden="true">
    <rect width="687" height="490" fill="var(--peach)"/>
    <path d="M0,0 H530 C640,40 700,120 672,232 C645,330 565,392 460,410 C380,424 300,430 220,418 C120,402 40,372 0,316 Z" fill="#fff"/>
    <line x1="227" y1="0" x2="227" y2="400" stroke="#e4e4e4" stroke-dasharray="2 2" stroke-width=".6"/>
    <line x1="453" y1="0" x2="453" y2="400" stroke="#e4e4e4" stroke-dasharray="2 2" stroke-width=".6"/>
  </svg>

  <!-- services panel -->
  <h2 class="abs script h-service" style="left:17px;top:14px">Blutegeltherapie</h2>
  <div class="abs body" style="left:18px;top:37px;width:200px">
    <div class="float-circle" style="margin-top:1px"></div>
    Blutegel gehören zu der Unterklasse der Egel (Hirudinea) und werden in der Medizin schon lange zur Behandlung verschiedener Krankheiten eingesetzt. Sie haben einen Saugnapf, mit dem sie sich an die zu behandelnden Stellen festsetzen und Blut saugen. Das Speichel-Sekret des Blutegels, welches beim Beissen in die Wunde des Tieres gelangt, wirkt entzündungs- und gerinnungshemmend, schmerzlindernd und regt den Lymphfluss an.
  </div>
  <div class="abs photo-circle" style="left:146px;top:43px;width:70px;height:70px"><div class="fill fill--dog" role="img" aria-label="Foto: Blutegel auf dem Fell eines Hundes"></div></div>
  <div class="badge" style="left:179px;top:37px;width:24px;height:24px">
    <svg width="12" height="12" viewBox="0 0 12 12" aria-hidden="true"><path d="M4 1 C2 4 6 6 4 11 M8 1 C6 4 10 6 8 11" stroke="#fff" stroke-width="1.4" fill="none"/></svg>
  </div>

  <h2 class="abs script h-service" style="left:17px;top:158px">Bachblütenberatung</h2>
  <span class="dot" style="left:190px;top:155px;width:8px;height:8px"></span>
  <p class="abs body" style="left:18px;top:184px;width:195px">Bachblüten sind Extrakte aus Blüten, die auf störende Emotionen und Gefühle wie z.B. (Trennungs-)Angst, Unsicherheit, Agression, Stress usw. positiv einwirken. Sie können bei Silvester, einer langen Autoreise, Umzug oder dem Tierarztbesuch unterstützen.</p>

  <h2 class="abs script h-service" style="left:17px;top:234px">Tierkommunikation</h2>
  <div class="abs photo-circle" style="left:18px;top:266px;width:70px;height:70px"><div class="fill fill--dog" style="background:linear-gradient(160deg,#e8e2dc,#6b3a22 55%,#f1ece6)" role="img" aria-label="Foto: Spaniel-Portrait"></div></div>
  <div class="badge" style="left:30px;top:260px;width:24px;height:24px">
    <svg width="10" height="11" viewBox="0 0 10 11" aria-hidden="true"><rect x="1" y="3" width="8" height="8" rx="1.5" fill="#fff"/><rect x="3" y="0.5" width="4" height="2" fill="#fff"/></svg>
  </div>
  <p class="abs body" style="left:98px;top:257px;width:122px">Nicht nur wir Menschen kämpfen oft mit seelischen Belastungen, unseren Tieren geht es häufig genauso. Die Tierkommunikation funktioniert über Telepathie. Telepathie bedeutet so viel wie Fernfühlen oder auch Fernwahrnehmen. Hierfür benötige ich lediglich ein bis zwei Fotos des Tieres.</p>

  <h2 class="abs script h-service" style="left:20px;top:349px">Edelsteintherapie</h2>
  <div class="abs body" style="left:18px;top:375px;width:200px">
    <div class="float-circle" style="margin-top:-6px"></div>
    Unsere Tiere reagieren auf unser Umfeld sensibler, als wir Menschen. Bei der Edelsteintherapie wird davon ausgegangen, dass die Heilsteine die Fähigkeiten besitzen seelische und körperliche Beschwerden zu mindern.
  </div>
  <div class="abs photo-circle" style="left:146px;top:368px;width:70px;height:70px"><div class="fill fill--stone" role="img" aria-label="Foto: Heilsteine auf dem Fell eines Hundes"></div></div>
  <div class="badge" style="left:189px;top:363px;width:24px;height:24px">
    <svg width="12" height="10" viewBox="0 0 12 10" aria-hidden="true"><path d="M3 0.5 H9 L11.5 3.5 L6 9.5 L0.5 3.5 Z" fill="#fff"/></svg>
  </div>

  <span class="dot" style="left:57px;top:442px;width:9px;height:9px"></span>
  <h2 class="abs script h-service" style="left:30px;top:437px">Mykotherapie</h2>
  <p class="abs body" style="left:18px;top:463px">Oder auch vereinfacht gesagt: Das Heilen mit Pilzen.</p>

  <!-- contact panel -->
  <div class="photo-frame" style="left:253px;top:38px;width:174px;height:186px"><div class="fill fill--garden" role="img" aria-label="Foto: Therapeutin sitzt mit ihrem Spaniel auf dem Rasen"></div></div>
  <h2 class="abs script center" style="left:240px;top:245px;width:200px;font-size:15px">Kontakt</h2>
  <p class="abs body center" style="left:240px;top:276px;width:200px">Termine nur nach Vereinbarung.</p>
  <p class="abs body center" style="left:240px;top:293px;width:200px;line-height:8.8px">Hier können wir gemeinsam entscheiden,<br>ob ihr zu mir in meine Praxis kommt<br>oder ich euch mit meiner mobilen<br>Praxis Zuhause besuche.</p>
  <svg class="abs" style="left:334px;top:350px" width="11" height="11" viewBox="0 0 24 24" aria-hidden="true"><path d="M6.6 10.8a15.1 15.1 0 006.6 6.6l2.2-2.2a1 1 0 011-.25 11.4 11.4 0 003.6.6 1 1 0 011 1V20a1 1 0 01-1 1A17 17 0 013 4a1 1 0 011-1h3.5a1 1 0 011 1c0 1.25.2 2.45.6 3.6a1 1 0 01-.25 1z" fill="#333"/></svg>
  <p class="abs body center" style="left:240px;top:365px;width:200px">0176 55501234</p>
  <p class="abs body center" style="left:240px;top:382px;width:200px;line-height:8.6px"><span style="color:var(--heading)">www.pfotenruhe-mitte.de</span><br>info@pfotenruhe-mitte.de<br>Lindenweg 7, 35390 Mittelstadt</p>

  <!-- cover panel -->
  <span class="abs" style="left:545px;top:64px;width:42px;height:42px;border:3px solid var(--accent);border-radius:50%"></span>
  <p class="abs brand-name center" style="left:486px;top:114px;width:160px">Pfotenruhe Mitte</p>
  <p class="abs brand-tag center" style="left:486px;top:132px;width:160px">Hundephysiotherapie<br>Lena Marwitz</p>
  <p class="abs script center" style="left:486px;top:192px;width:160px;font-size:9.5px;color:#333;font-weight:500;line-height:12px">“Lebensfreude lässt sich am besten<br>von Hunden lernen.”</p>
  <p class="abs script center" style="left:486px;top:220px;width:160px;font-size:7px;font-weight:500">(Tom Berger)</p>
  <div class="photo-frame" style="left:480px;top:237px;width:172px;height:200px"><div class="fill fill--spaniel" role="img" aria-label="Foto: schwarz-weißer Spaniel sitzt auf der Wiese"></div></div>
  <p class="abs services" style="left:456px;top:447px">Hundephysiotherapie • Hundeosteopathie i.A. • Hundefitnesstrainerin<br>Bachblütenberaterin • Tierkommunikation • Tierkommunikation<br>Mykotherapie • Edelsteintherapie</p>
</section>

<!-- Inside -->
<section class="sheet sheet--inside">
  <div class="abs" style="left:234px;top:0;width:226px;height:490px;background:var(--peach-light)"></div>

  <!-- left -->
  <h3 class="abs script" style="left:18px;top:28px;font-size:10.5px;font-weight:500">Leben ist Bewegung und Bewegung ist Lebensqualität!</h3>
  <p class="abs body" style="left:18px;top:50px;width:204px">Rennen, laufen, springen, toben und spielen zeigt die Lebensfreude unserer Hunde! Wer keine Schmerzen hat, kann sich frei bewegen und hat Spaß dabei. Wenn unsere Hunde jedoch erkranken oder alt werden, dann benötigen sie unsere Unterstützung.</p>
  <div class="photo-frame" style="left:18px;top:99px;width:78px;height:112px"><div class="fill fill--lawn" role="img" aria-label="Foto: Therapeutin behandelt einen Schäferhund im Gras"></div></div>
  <p class="abs body" style="left:106px;top:102px;width:118px">Nach einem Unfall, bei Schmerzen oder Beschwerden im Rücken und in den Gelenken, nach Operationen oder bei Lahmheiten können Physiotherapie sowie Osteopathie helfen. Es lindert die Schmerzen, lockert verspannte Muskulatur, verbessert die Beweglichkeit oder stellt diese wiederher. Weiterhin baut Physiotherapie Muskulatur auf, fördert die Genesung und hilft im Alter fit zu bleiben.</p>
  <p class="abs body" style="left:18px;top:220px;width:210px">Ich helfe Deinem Hund  gerne dabei, die Gesundheit und damit die Lebensqualität und Lebensfreude zurück zu erhalten.</p>
  <p class="abs script" style="left:150px;top:237px;width:74px;text-align:right;font-size:9.5px;color:#333;font-weight:500">Lena Marwitz</p>
  <span class="dot" style="left:144px;top:243px;width:12px;height:12px"></span>
  <h3 class="abs script" style="left:18px;top:259px;font-size:10px;font-weight:500;line-height:12.5px">Doch nicht nur die Hundephysiotherapie verhilft<br>Deinem Hund zu mehr Vitalität ...</h3>
  <span class="dot" style="left:200px;top:274px;width:8px;height:8px"></span>
  <span class="dot" style="left:159px;top:282px;width:9px;height:9px"></span>
  <p class="speech" style="top:292px">Ist Dein Hund ängstlich, ihm geht es nicht gut oder Du wirst aus verschiedenen Verhaltensweisen nicht schlau?</p>
  <p class="abs body" style="left:18px;top:328px;width:206px">Hier greift zum Beispiel die Tierkommunikation oder Bachblüten. Auch die Vitalpilz-Therapie wird in dem Veterinärbereich immer wichtiger, da hier grandiose Erfolge erzielt werden. U.a. bei Verdauungsproblemen, Immunstörungen, Allergie,  Arthrose, Durchblutungsstörungen oder sogar Krebs und Mittelmeerkrankheiten.</p>
  <p class="speech" style="top:390px">Ist Dein Hund gesund, Du möchtest nur seine Fitness verbessern oder ein paar Kilos sollen schwinden?</p>
  <p class="abs body" style="left:18px;top:428px;width:206px">Hier unterstütze ich euch gerne mit meinen Hundefitnesstrainer Kenntnissen. Wir arbeiten gemeinsam einen Trainingsplan für Deinen Hund heraus. Sei es für den Sporthund in Agility oder für die Couchpotato.</p>

  <!-- middle -->
  <div class="photo-frame" style="left:245px;top:31px;width:62px;height:68px;border-radius:9px;padding:3px"><div class="fill fill--lawn" role="img" aria-label="Foto: Therapeutin mit Hund im Garten"></div></div>
  <div class="photo-frame" style="left:316px;top:31px;width:62px;height:68px;border-radius:9px;padding:3px"><div class="fill fill--puppy" role="img" aria-label="Foto: Welpe wird behandelt"></div></div>
  <div class="photo-frame" style="left:387px;top:31px;width:62px;height:68px;border-radius:9px;padding:3px"><div class="fill fill--lawn" style="background:linear-gradient(180deg,#6d8f3e 0,#3a3a3a 45%,#c04fa6 85%)" role="img" aria-label="Foto: Hund trainiert auf Balancepads"></div></div>
  <h2 class="abs script center" style="left:237px;top:122px;width:220px;font-size:14.5px;line-height:15px">Hundephysiotherapie &amp;<br>Hundeosteopathie (i.A.)</h2>
  <p class="abs body center" style="left:240px;top:167px;width:214px;line-height:10.4px">In der Humanmedizin wird die Physiotherapie bei der Genesung der Patienten schon selbstverständlich und unterstützend eingesetzt. Tiere können an ähnlichen Problemen leiden wie wir Menschen. Sie haben genau so Schmerzen und dies schränkt ihr Leben oftmals ein. Wir können unsere Schmerzen äußern. Viele Hunde jedoch leben mit diesem Schmerz viele Wochen, ehe es unerträglich wird und sie lahmen oder andere Dinge anzeigen. Gerade deshalb ist die Physiotherapie so enorm wichtig, damit unsere Hunde unbeschwert und ohne Schmerzen lange an unserer Seite bleiben.</p>
  <p class="abs body center" style="left:240px;top:287px;width:214px;line-height:10.4px">Jeder Körper ist ein individuelles und komplexes System mit eigenen Anforderungen an Beanspruchungen, Intensitäten und Erholungsphasen. Entsprechend umfangreich aufgestellt ist das Therapiespektrum meiner Arbeit.</p>
  <p class="abs body center" style="left:240px;top:347px;width:214px;line-height:10.4px">Dabei immer im Fokus: Die stets vollkommen individuellen Therapieprogramme, in enger Zusammenarbeit mit dem Tierarzt. Sensibel abgestimmt auf die spezifischen Anforderungen der einzelnen Krankheitsbilder. Jeder Hund hat eine andere Hintergrundgeschichte und auch dies berücksichtige ich bei meinen Therapien.</p>
  <p class="abs script center" style="left:240px;top:428px;width:214px;font-size:10px;font-weight:500;line-height:12.5px">Mein Ziel ist es, die Lebensfreude und Lebensqualität unserer Vierbeiner zu erhalten oder gar zu verbessern.</p>

  <!-- right -->
  <h2 class="abs script center" style="left:463px;top:27px;width:220px;font-size:15px">Dorn Therapie und Breuß Massage</h2>
  <p class="abs body" style="left:471px;top:52px;font-weight:500">• Breuß-Massage:</p>
  <p class="abs body" style="left:471px;top:70px;width:205px">Bei der Breuß-Massage wird die Wirbelsäule durch eine wohltuende Massage am Kreuzbein entspannt und gestreckt. Durch gezielte Griffe und Dehnungen wird der Rücken gelockert und verschobene Wirbel schmerzfrei in die ursprüngliche Position gebracht.</p>
  <p class="abs body" style="left:471px;top:127px;font-weight:500">• Dorn-Therapie:</p>
  <p class="abs body" style="left:471px;top:145px;width:205px">Die Wirbelsäulentherapie nach Dorn, ist eine sanfte Methode, die zur Behandlung von Beschwerden des Bewegungsapparates zum Einsatz kommt. Der Therapeut bringt in der Therapiesitzung Wirbel und Gelenke mit sanften und einfühlsamen Bewegungen in ihre richtige Position zurück.</p>
  <div class="abs photo-circle" style="left:488px;top:205px;width:164px;height:164px"><div class="fill fill--lawn" role="img" aria-label="Foto: Therapeutin massiert den Rücken eines liegenden Spaniels"></div></div>
  <h2 class="abs script center" style="left:463px;top:379px;width:220px;font-size:14.5px">Hundefitnesstrainer (i.A.)</h2>
  <ul class="abs list" style="left:471px;top:406px;width:115px">
    <li>• Individuelle Trainingspläne</li>
    <li>• Muskelaufbautraining</li>
    <li>• Beweglichkeitstraining</li>
    <li>• Abnehmtraining</li>
    <li>• Fitnesstraining</li>
    <li>• Gehirntraining</li>
  </ul>
  <ul class="abs list" style="left:588px;top:406px;width:92px">
    <li>• Schult den optimalen Bewegungsablauf</li>
    <li>• Tipps und Training für Sporthunde</li>
    <li>• z.B. mit Cavaletti oder Balancepads</li>
  </ul>
</section>

</body>
</html>
```